Home page concept, possible logo colour change

There is no need to code a home page, we are just looking for concept ideas.
We have had a logo designed for a new company we are starting named Corvenhall Aluminium Windows & Doors. We are manufacturing bullet resistant window frames. We have had logo designed, we like the concept of the design, but the current colours (black and red) may not be the best option, especially when designing the website home page, and how it interacts with the logo colours. I have also attached the first draft of the home page which we are not happy with. The overall design/navigation is good, we have issues with the darkened out primary image and also the amount of red on the page, it just doesn't feel right. As mentioned before we are happy to look at colour changes to the logo.
Number of Pages Required
1 page
Look and feel
Each slider illustrates characteristics of the customer's brand and the style your logo design should communicate.

```html
<!DOCTYPE html>
<html lang="en">
<head>
<meta charset="utf-8">
<title>Corvenhall Aluminium Windows &amp; Doors</title>
<link href="https://fonts.googleapis.com/css2?family=Poppins:wght@300;400;500;600;700&display=swap" rel="stylesheet">
<style>
:root{
  --blue:#1f86cf;
  --blue-dark:#0b3c74;
  --ink:#1b1b1b;
  --muted:#6b6b6b;
  --line:#dcdcdc;
  --bg:#ffffff;
  --hero-a:#0a3566;
  --hero-b:#2f7dc4;
  --hero-c:#8cc3ea;
}
*{box-sizing:border-box;margin:0;padding:0}
html,body{width:1200px;height:2384px;overflow:hidden;background:var(--bg);font-family:'Poppins',sans-serif;color:var(--ink)}
.page{position:relative;width:1200px;height:2384px}
.abs{position:absolute}

.site-header{position:absolute;left:0;top:0;width:1200px;height:56px;display:flex;align-items:center;justify-content:space-between;padding:0 56px}
.brand{display:flex;align-items:center;gap:8px;font-weight:600;font-size:15px;color:var(--blue-dark)}
.brand-mark{width:14px;height:14px;background:var(--blue)}
.main-nav{display:flex;gap:28px;font-size:12px}
.main-nav a{color:var(--ink);text-decoration:none;padding-bottom:4px}
.main-nav a.active{border-bottom:2px solid var(--ink)}

.hero{position:absolute;left:0;top:56px;width:1200px;height:616px;background:linear-gradient(160deg,var(--hero-a) 0%,var(--hero-b) 45%,var(--hero-c) 75%,var(--hero-b) 100%)}
.hero-title{position:absolute;top:224px;width:100%;text-align:center;color:#fff;font-weight:600;font-size:50px}
.hero-sub{position:absolute;top:300px;width:100%;text-align:center;color:#fff;font-weight:300;font-size:38px}
.hero-btn{position:absolute;left:476px;top:432px;width:208px;height:50px;border:2px solid #fff;color:#fff;font-weight:500;font-size:17px;display:flex;align-items:center;justify-content:center}

.features{position:absolute;top:740px;left:0;width:1200px}
.feature{position:absolute;width:180px;text-align:center}
.feature svg{display:block;margin:0 auto 18px}
.feature h3{font-size:14px;font-weight:500;margin-bottom:6px}
.feature p{font-size:11px;color:var(--muted);line-height:1.5}

.section-title{position:absolute;top:1020px;width:100%;text-align:center;font-size:32px;font-weight:500}

.card{position:absolute;top:1092px;width:264px}
.card-media{width:264px;height:268px;background:linear-gradient(#f3f3f3,#e2e2e2)}
.card-media.scene{background:linear-gradient(180deg,#c9d8e6 0%,#8ea9b8 50%,#5f6f5a 100%)}
.card h4{font-size:15px;font-weight:500;margin:14px 0 6px}
.card p{font-size:11px;color:var(--muted);line-height:1.55}
.card a{display:block;margin-top:12px;font-size:11px;color:var(--blue);text-decoration:none;font-weight:500}

.showcase-media{position:absolute;left:236px;top:1620px;width:270px;height:280px;background:linear-gradient(#f4f4f4,#e4e4e4)}
.accordion{position:absolute;left:608px;top:1620px;width:336px}
.acc-item{display:flex;justify-content:space-between;align-items:center;height:44px;border-bottom:1px solid var(--line);font-size:14px;font-weight:500}
.acc-item span.sign{color:var(--blue);font-size:22px;font-weight:400}
.acc-body{font-size:11px;color:var(--muted);line-height:1.6;padding:12px 0}

.enquiry{position:absolute;top:2010px;left:248px;width:704px;display:flex;align-items:center;gap:20px}
.enquiry-label{color:var(--blue);font-size:18px;font-weight:500;width:168px}
.enquiry-input{width:392px;height:40px;border:1px solid var(--line);font-size:12px;color:#aaa;display:flex;align-items:center;padding:0 14px}
.enquiry-btn{width:84px;height:40px;background:var(--blue);color:#fff;font-weight:600;font-size:15px;display:flex;align-items:center;justify-content:center}

.site-footer{position:absolute;top:2130px;left:0;width:1200px;height:254px;border-top:1px solid var(--line)}
.footer-brand{position:absolute;left:216px;top:60px;display:flex;align-items:center;gap:10px;font-weight:600;font-size:22px;color:var(--blue-dark)}
.footer-brand .brand-mark{width:20px;height:20px}
.footer-nav{position:absolute;left:496px;top:40px;font-size:12px;line-height:2.9}
.footer-contact{position:absolute;left:680px;top:40px;font-size:11px;line-height:1.5}
.footer-contact h5,.footer-qa h5{font-size:12px;font-weight:600}
.footer-contact p{margin-bottom:14px;color:#333}
.footer-qa{position:absolute;left:912px;top:40px;text-align:center}
.qa-badge{width:48px;height:48px;border-radius:50%;background:#2e8a3e;margin:12px auto 0}
.copyright{position:absolute;left:0;bottom:0;width:1200px;height:34px;border-top:1px solid var(--line);font-size:10px;color:var(--muted);display:flex;align-items:center;justify-content:center}
</style>
</head>
<body>
<div class="page">

<header class="site-header">
  <div class="brand"><span class="brand-mark"></span>Corvenhall</div>
  <nav class="main-nav">
    <a class="active" href="#">Home</a>
    <a href="#">Our Products</a>
    <a href="#">Why Corvenhall</a>
  </nav>
</header>

<section class="hero" role="img" aria-label="Blue glass facade of a modern office building">
  <h1 class="hero-title">Bullet Resistant window &amp; Doors</h1>
  <p class="hero-sub">Your First Line of Defence</p>
  <div class="hero-btn">Make an Enquiry</div>
</section>

<section class="features">
  <div class="feature" style="left:278px">
    <svg width="52" height="56" viewBox="0 0 52 56" fill="none" stroke="#222" stroke-width="2"><path d="M26 3 L47 11 V27 C47 40 37 49 26 53 C15 49 5 40 5 27 V11 Z"/><path d="M17 28 L24 35 L36 21"/></svg>
    <h3>Premium Protection</h3>
    <p>Frames tested and certified to rated threat levels.</p>
  </div>
  <div class="feature" style="left:502px">
    <svg width="56" height="56" viewBox="0 0 56 56" fill="none" stroke="#222" stroke-width="2"><rect x="22" y="3" width="22" height="22"/><rect x="8" y="18" width="20" height="20"/><rect x="24" y="32" width="20" height="20"/></svg>
    <h3>Aesthetically Designed</h3>
    <p>Slim profiles finished to suit any modern facade.</p>
  </div>
  <div class="feature" style="left:734px">
    <svg width="64" height="56" viewBox="0 0 64 56" fill="none" stroke="#222" stroke-width="2"><rect x="4" y="12" width="34" height="26"/><path d="M38 20 H50 L58 30 V38 H38"/><circle cx="15" cy="42" r="5"/><circle cx="48" cy="42" r="5"/><path d="M0 20 H10 M0 28 H8"/></svg>
    <h3>Promptly Delivered</h3>
    <p>Made to order and delivered on schedule nationwide.</p>
  </div>
</section>

<h2 class="section-title">Superior Protection, Sleek Design</h2>

<article class="card" style="left:172px">
  <div class="card-media" role="img" aria-label="Black framed single window product"></div>
  <h4>Product</h4>
  <p>Single-pane bullet resistant windows built with reinforced aluminium frames and laminated glazing for homes, offices and secure public buildings.</p>
  <a href="#">Learn more</a>
</article>
<article class="card" style="left:468px">
  <div class="card-media" role="img" aria-label="Black framed multi-panel door product"></div>
  <h4>Product</h4>
  <p>Multi-panel door systems combining protection with clear sightlines, engineered to match residential and commercial interiors without visible bulk.</p>
  <a href="#">Learn more</a>
</article>
<article class="card" style="left:764px">
  <div class="card-media scene" role="img" aria-label="Interior with large glazed window overlooking a lake"></div>
  <h4>Enquiry</h4>
  <p>Tell us about your project and our team will recommend the right rating, frame profile and glazing for your site and budget.</p>
  <a href="#">Enquiry Now</a>
</article>

<div class="showcase-media" role="img" aria-label="Black framed facade window unit"></div>
<div class="accordion">
  <div class="acc-item">Window Systems<span class="sign">+</span></div>
  <div class="acc-item">Sliding Systems<span class="sign">+</span></div>
  <div class="acc-item">Door Systems<span class="sign">+</span></div>
  <div class="acc-item">Facade Systems<span class="sign">&minus;</span></div>
  <p class="acc-body">Our facade systems combine structural aluminium framing with certified ballistic glazing, giving large glazed elevations the same protection as our windows and doors while keeping a light, open appearance for architects and owners alike.</p>
</div>

<div class="enquiry">
  <div class="enquiry-label">Make an Enquiry</div>
  <div class="enquiry-input">Your email</div>
  <div class="enquiry-btn">Send</div>
</div>

<footer class="site-footer">
  <div class="footer-brand"><span class="brand-mark"></span>Corvenhall</div>
  <nav class="footer-nav">
    <div>Home</div><div>Our Products</div><div>Why Corvenhall</div><div>Blog</div>
  </nav>
  <div class="footer-contact">
    <h5>Sydney</h5>
    <p>48 Harbourline Street<br>Sydney NSW 2010</p>
    <h5>Contact us</h5>
    <p>T: +61 (0)2 9312 4800<br>E: info@corvenhall.com.au</p>
  </div>
  <div class="footer-qa">
    <h5>Quality Assurance</h5>
    <div class="qa-badge"></div>
  </div>
  <div class="copyright">Copyright &copy; 2024 Corvenhall. All Rights Reserved.</div>
</footer>

</div>
</body>
</html>
```